New retail box design

We are looking at changing our packaging for retilers. I have templates of boxes and like a great design for new packaging.

I will attach pictures of our current packaging.

Industry/Entity Type

Ammunition manufacturing

Requirements
Must have
• warning label and company name

```html
<!DOCTYPE html>
<html lang="en">
<head>
<meta charset="utf-8">
<title>Liberty Forge Ammo Co. – 09-MM Retail Box</title>
<link rel="stylesheet" href="https://fonts.googleapis.com/css2?family=Michroma&family=Montserrat:wght@500;600&family=Oswald:wght@500&family=Roboto+Condensed:wght@300;400&display=swap">
<style>
  :root {
    --stage: #2b2b2b;
    --panel: #161616;
    --panel-edge: #1e1e1e;
    --rule: #8a8a8a;
    --orange: #f07a28;
    --orange-dim: #7a4a30;
    --white: #f2f2f2;
    --grey-text: #9a9a9a;
    --numeral: #d8d8d8;
    --eagle-blue: #2f4a78;
    --flag-red: #b8343c;
  }
  * { margin: 0; padding: 0; box-sizing: border-box; }
  html, body { width: 1200px; height: 1109px; overflow: hidden; background: var(--stage); }
  .canvas { position: relative; width: 1200px; height: 1109px; }

  .panel {
    position: absolute;
    background: var(--panel);
    border: 1px solid var(--panel-edge);
  }
  .panel svg.frame { position: absolute; inset: 0; }

  /* top panel */
  .top-panel { left: 400px; top: 70px; width: 740px; height: 150px; }
  .top-artwork {
    position: absolute; left: 150px; top: 35px; width: 440px; height: 80px;
    border-radius: 40px;
    background: linear-gradient(90deg, var(--eagle-blue) 0%, #3d5f94 45%, #c9c9d2 62%, var(--flag-red) 80%, var(--eagle-blue) 100%);
    opacity: 0.85;
  }

  /* side panel */
  .side-panel { left: 70px; top: 230px; width: 330px; height: 760px; }
  .warning-label {
    position: absolute; left: 38px; top: 80px; width: 140px; height: 100px;
    border: 1px solid var(--orange);
    font-family: "Roboto Condensed", sans-serif;
  }
  .warning-label .warning-title {
    color: var(--orange); font-size: 11px; letter-spacing: 0.5px;
    padding: 6px 8px; border-bottom: 1px solid var(--orange);
  }
  .warning-label .warning-text {
    color: var(--grey-text); font-size: 11px; line-height: 1.3;
    padding: 8px 8px; width: 80px;
  }
  .warning-label svg { position: absolute; right: 14px; bottom: 22px; }
  .safety-heading {
    position: absolute; left: 40px; top: 238px;
    font-family: "Oswald", sans-serif; font-weight: 500;
    color: var(--orange); font-size: 20px; letter-spacing: 1px;
  }
  .safety-rules {
    position: absolute; left: 38px; top: 300px; width: 260px;
    list-style: none;
    font-family: "Roboto Condensed", sans-serif; font-weight: 300;
    color: var(--grey-text); font-size: 15px; line-height: 1.38;
  }
  .safety-rules li { position: relative; padding-left: 14px; }
  .safety-rules li::before {
    content: ""; position: absolute; left: 0; top: 8px;
    width: 4px; height: 4px; background: var(--orange);
  }

  /* front panel */
  .front-panel { left: 400px; top: 230px; width: 740px; height: 760px; }
  .brand-name {
    position: absolute; left: 56px; top: 112px;
    font-family: "Michroma", sans-serif; font-weight: 400; color: var(--white);
    font-size: 32px; line-height: 1.25; letter-spacing: 1px;
  }
  .brand-name .brand-sub { display: block; font-size: 32px; }
  .brand-name .brand-tag { display: block; font-size: 16px; letter-spacing: 3px; margin-top: 6px; }
  .brand-mark {
    position: absolute; left: 58px; top: 250px; width: 22px; height: 22px;
    background: var(--white);
  }
  .calibre {
    position: absolute; left: 118px; top: 562px;
    font-family: "Montserrat", sans-serif; font-weight: 600;
    font-size: 76px; letter-spacing: 1px; line-height: 1;
  }
  .calibre .calibre-num { color: var(--numeral); }
  .calibre .calibre-unit { color: var(--orange); }
  .calibre-arrow { position: absolute; left: 52px; top: 572px; }
  .product-details {
    position: absolute; left: 62px; top: 690px;
    font-family: "Montserrat", sans-serif; font-weight: 500;
    color: var(--orange); font-size: 13px; line-height: 1.3;
  }
</style>
</head>
<body>
<main class="canvas">

  <!-- Top panel: lid artwork -->
  <section class="panel top-panel" aria-label="Box top panel">
    <div class="top-artwork" role="img" aria-label="Eagle with flag illustration"></div>
  </section>

  <!-- Side panel: warnings and safety rules -->
  <section class="panel side-panel" aria-label="Box side panel">
    <svg class="frame" width="330" height="760" viewBox="0 0 330 760" aria-hidden="true">
      <line x1="20" y1="0" x2="20" y2="760" stroke="var(--rule)" stroke-width="1"/>
      <line x1="0" y1="60" x2="330" y2="60" stroke="var(--rule)" stroke-width="1"/>
      <line x1="0" y1="725" x2="330" y2="725" stroke="var(--rule)" stroke-width="1"/>
      <path d="M14 40h12M20 34v12" stroke="var(--orange)" stroke-width="2"/>
      <path d="M34 30l6 6 6-6M44 30l6 6 6-6" stroke="var(--orange)" stroke-width="2" fill="none"/>
      <path d="M38 230v40l90 14" stroke="var(--orange)" stroke-width="1.5" fill="none"/>
      <circle cx="128" cy="284" r="2.5" fill="var(--orange)"/>
    </svg>
    <div class="warning-label">
      <div class="warning-title">WARNING</div>
      <p class="warning-text">Keep out of reach of children.</p>
      <svg width="16" height="14" viewBox="0 0 16 14" aria-hidden="true">
        <path d="M8 0L16 14H0Z" fill="var(--orange)"/>
        <rect x="7.2" y="4" width="1.6" height="5" fill="var(--panel)"/>
        <rect x="7.2" y="10.5" width="1.6" height="1.6" fill="var(--panel)"/>
      </svg>
    </div>
    <h2 class="safety-heading">SAFETY RULES:</h2>
    <ul class="safety-rules">
      <li>Watch your muzzle. Keep gun pointed in safe direction.</li>
      <li>Wear eye and ear protection.</li>
      <li>If gun fails to fire, keep it pointed in a safe direction, then unload carefully avoiding exposure to breech.</li>
      <li>Know your target and what is beyond it.</li>
      <li>Treat every gun as if it were loaded. Don't rely on the safety.</li>
      <li>Keep barrel clear of obstructions.</li>
      <li>Never load a gun until ready to use.</li>
      <li>Only use ammunition that exactly matches marking of your gun.</li>
    </ul>
  </section>

  <!-- Front panel -->
  <section class="panel front-panel" aria-label="Box front panel">
    <svg class="frame" width="740" height="760" viewBox="0 0 740 760" aria-hidden="true">
      <defs>
        <radialGradient id="holeTone" cx="50%" cy="50%" r="50%">
          <stop offset="0" stop-color="#3a3a3a"/>
          <stop offset="0.45" stop-color="#e6e6e6"/>
          <stop offset="1" stop-color="#777"/>
        </radialGradient>
        <linearGradient id="brassTone" x1="0" y1="0" x2="0" y2="1">
          <stop offset="0" stop-color="#b8663a"/>
          <stop offset="0.35" stop-color="#c9a24a"/>
          <stop offset="1" stop-color="#8a7030"/>
        </linearGradient>
      </defs>
      <!-- frame -->
      <line x1="30" y1="0" x2="30" y2="760" stroke="var(--rule)"/>
      <line x1="710" y1="0" x2="710" y2="760" stroke="var(--rule)"/>
      <line x1="0" y1="40" x2="740" y2="30" stroke="var(--rule)"/>
      <line x1="0" y1="728" x2="740" y2="718" stroke="var(--rule)"/>
      <!-- corner crosses -->
      <path d="M20 40h20M30 30v20M700 30h20M710 20v20M20 728h20M30 718v20M700 718h20M710 708v20M20 654h20M30 644v20" stroke="var(--orange)" stroke-width="2"/>
      <!-- top band -->
      <path d="M30 72H280L296 92H712" stroke="var(--orange)" stroke-width="2.5" fill="none"/>
      <g fill="var(--orange)">
        <path d="M300 64h16l10 16h-16z"/>
        <path d="M384 62h16l10 16h-16z"/>
        <path d="M468 60h16l10 16h-16z"/>
        <path d="M552 58h16l10 16h-16z"/>
        <path d="M636 56h16l10 16h-16z"/>
        <path d="M678 56h16l10 16h-16z"/>
      </g>
      <g fill="var(--orange-dim)">
        <path d="M342 63h16l10 16h-16z"/>
        <path d="M426 61h16l10 16h-16z"/>
        <path d="M510 59h16l10 16h-16z"/>
        <path d="M594 57h16l10 16h-16z"/>
      </g>
      <!-- impact marks artwork -->
      <g role="img" aria-label="Bullet hole impact marks">
        <circle cx="500" cy="148" r="34" fill="url(#holeTone)"/>
        <circle cx="618" cy="140" r="36" fill="url(#holeTone)"/>
        <circle cx="580" cy="245" r="32" fill="url(#holeTone)"/>
        <circle cx="612" cy="345" r="33" fill="url(#holeTone)"/>
      </g>
      <!-- cartridge artwork -->
      <rect x="420" y="400" width="170" height="232" rx="6" fill="url(#brassTone)" opacity="0.85" role="img" aria-label="Three brass rifle cartridges standing upright"/>
      <!-- crossed boxes -->
      <g stroke="#6a6a6a" stroke-width="1.2" fill="none">
        <rect x="68" y="420" width="46" height="50"/>
        <path d="M68 420l46 50M114 420l-46 50"/>
        <rect x="114" y="460" width="86" height="94"/>
        <path d="M114 460l86 94M200 460l-86 94"/>
      </g>
      <!-- bottom band -->
      <path d="M30 658H150L165 650H400L480 700V740" stroke="var(--orange)" stroke-width="2.5" fill="none"/>
    </svg>

    <h1 class="brand-name">LIBERTY<span class="brand-sub">FORGE</span><span class="brand-tag">AMMO CO.</span></h1>
    <span class="brand-mark" aria-hidden="true"></span>

    <svg class="calibre-arrow" width="56" height="62" viewBox="0 0 56 62" aria-hidden="true">
      <path d="M4 8L28 32L4 56M18 4L46 32L18 60" stroke="var(--orange)" stroke-width="6" fill="none"/>
    </svg>
    <p class="calibre"><span class="calibre-num">09</span><span class="calibre-unit">-MM</span></p>

    <p class="product-details">PRODUCT DETIALS<br>GOES HERE</p>
  </section>

</main>
</body>
</html>
```